Property Management Company looking for a high-end business card, letterhead and envelope design.

We provide high-end / boutique property management for real estate investors or individuals looking for someone to manage their portfolio. we are looking for a cohesive high-end design for our business cards, letterhead and envelopes.

Target Market(s)

Real Estate Investors

Industry/Entity Type

Real Estate

Requirements
Must have
• business card, letterhead and envelope design - logo attached

```html
<!DOCTYPE html>
<html lang="en">
<head>
<meta charset="utf-8">
<title>Orvale Property Management – Business Card</title>
<link rel="stylesheet" href="https://fonts.googleapis.com/css2?family=Montserrat:wght@500;600;700&family=Arimo:wght@400;700&display=swap">
<style>
  :root {
    --stage: #1b1817;
    --card: #0c0c0c;
    --brand-blue: #165a9c;
    --steel: #b8b8b8;
    --text-light: #d6d6d6;
    --rule: #4a4a4a;
  }
  * { margin: 0; padding: 0; box-sizing: border-box; }
  html, body {
    width: 1200px; height: 842px; overflow: hidden;
    background: var(--stage);
  }
  .stage {
    position: relative; width: 1200px; height: 842px;
    display: flex; align-items: center; justify-content: center; gap: 40px;
  }
  .card {
    position: relative; width: 520px; height: 297px;
    background: var(--card);
    box-shadow: 0 12px 30px rgba(0,0,0,.55);
    overflow: hidden;
  }
  /* Contact side */
  .card--contact .band {
    position: absolute; left: 0; right: 0; height: 14px;
    background: var(--brand-blue);
  }
  .card--contact .band--top { top: 0; }
  .card--contact .band--bottom { bottom: 0; }
  .contact-block {
    position: absolute; left: 150px; top: 62px; width: 260px;
    font-family: "Arimo", Arial, sans-serif; color: var(--text-light);
  }
  .person-name {
    font-family: "Montserrat", sans-serif; font-weight: 700;
    font-size: 19px; color: var(--brand-blue); letter-spacing: .3px;
    line-height: 1;
  }
  .person-role { font-size: 13px; margin-top: 4px; padding-left: 26px; }
  .divider { height: 1px; background: var(--rule); margin: 9px 0 9px 26px; width: 190px; }
  .contact-list { list-style: none; font-size: 13.5px; line-height: 1.35; padding-left: 26px; }
  .contact-list .label { color: var(--brand-blue); font-weight: 700; margin-right: 4px; }
  .contact-list .web { color: var(--brand-blue); }
  .address { font-size: 14px; line-height: 1.35; padding-left: 26px; }

  /* Brand side */
  .tab { position: absolute; display: flex; height: 48px; }
  .tab .block { width: 30px; background: var(--brand-blue); }
  .tab .stripe { width: 4px; background: var(--steel); }
  .tab--left { left: 0; top: 168px; }
  .tab--right { right: 0; top: 40px; flex-direction: row-reverse; }
  .brand-name {
    position: absolute; left: 0; right: 0; top: 122px; text-align: center;
    font-family: "Montserrat", sans-serif; font-weight: 600;
    color: var(--brand-blue); letter-spacing: 4px; line-height: 1.2;
  }
  .brand-name .main { display: block; font-size: 30px; }
  .brand-name .sub { display: block; font-size: 12px; letter-spacing: 5px; }
</style>
</head>
<body>
<main class="stage">
  <section class="card card--contact" aria-label="Business card, contact side">
    <div class="band band--top"></div>
    <div class="contact-block">
      <h1 class="person-name">DANIEL HARTLEY</h1>
      <p class="person-role">Managing Director</p>
      <div class="divider"></div>
      <ul class="contact-list">
        <li><span class="label">P:</span>055-987 654 321</li>
        <li><span class="label">M:</span>055-987 654 321</li>
        <li><span class="label">E:</span>hello@orvalehomes.com</li>
        <li class="web">www.orvalehomes.com</li>
      </ul>
      <div class="divider"></div>
      <p class="address">12345, Address Goes Here<br>Country Name, 123456</p>
    </div>
    <div class="band band--bottom"></div>
  </section>

  <section class="card card--brand" aria-label="Business card, brand side">
    <div class="tab tab--left"><span class="block"></span><span class="stripe"></span></div>
    <div class="tab tab--right"><span class="block"></span><span class="stripe"></span></div>
    <p class="brand-name"><span class="main">ORVALE</span><span class="sub">PROPERTY MANAGEMENT</span></p>
  </section>
</main>
</body>
</html>
```